Retail Appliance Store Chain needs NEW business Card

Name of my company is Brandon's Appliances brandonsappliances.com is our website. . We are a 2 location brick and mortar, and online store selling premium, luxury, and normal household appliances, such as ovens, stoves, cooktops, dishwashers, refrigerators, washers and dryers, grills, air conditioners etc. The focus is on large kitchen appliances and laundry appliances.
Please visit http://brandonsappliances.com to get a feel for the business and branding.
I have attached the Brandon's Appliances logo (i do not have eps or psd or ai). And I have also attached our current business cards that we use. We have two versions. A double sided version for managers, and a one side version for regular employees.
Please submit BOTH one sided and two sided designs if possible.
Please keep consistent with the Brandon's Appliances logo, colors, etc.
I would prefer no rounded corners on the business card designs for printing costs.
Information on the cards (in no particular order):
Name - Employee Name
Business name - Brandon's Appliances
website - brandonsappliances.com
Email - Employee Email
2 Phone Numbers - store 1 address, store 2 address
2 Addresses - store 1 address, store 2 address

*do NOT need Fax #

Industry/Entity Type

Home Appliance

Contact Information for Business Card

Logo - Brandons Appliances Logo
Name - Employee Name
Email - Employee Email

Please no rounded corners. Standard US Business Card Size please.

Font styles to use
Serif
Sans Serif

Requirements
Must have
• colors and design that somewhat match the feel of current logo and website
Should not have
• No rounded corners.
No non-traditional business card size. US Standard Business Card Size only

```html
<!DOCTYPE html>
<html lang="en">
<head>
<meta charset="utf-8">
<title>Brandon's Appliances – Business Card</title>
<link rel="stylesheet" href="https://fonts.googleapis.com/css2?family=Montserrat:wght@500;600;800&family=Lato:wght@400;700&display=swap">
<style>
  :root {
    --brand-blue: #2a4ea3;
    --brand-blue-dark: #223f86;
    --ink: #1b1b1d;
    --paper: #ffffff;
    --text: #2a2a2a;
    --stage: #e4e6ea;
  }
  * { box-sizing: border-box; margin: 0; padding: 0; }
  html, body { width: 1200px; height: 900px; overflow: hidden; }
  body {
    background: var(--stage);
    font-family: "Lato", Arial, sans-serif;
    position: relative;
  }
  .card {
    position: absolute;
    width: 525px;
    height: 300px;
    overflow: hidden;
    box-shadow: 0 6px 18px rgba(0,0,0,.18);
  }
  /* ---------- Front ---------- */
  .card--front { left: 40px; top: 300px; background: var(--paper); }
  .front__photo {
    position: absolute; inset: 0;
    background: linear-gradient(135deg, #f7f7f7 0%, #e6e7e8 45%, #f3f3f2 70%, #dcdddd 100%);
    opacity: .9;
  }
  .front__corner { position: absolute; width: 48px; height: 48px; background: var(--ink); }
  .front__corner--top { left: 0; top: 0; clip-path: polygon(0 0, 100% 0, 100% 30%, 30% 100%, 0 100%); }
  .front__corner--bottom { left: 0; bottom: 0; clip-path: polygon(0 0, 30% 0, 100% 70%, 100% 100%, 0 100%); }
  .wordmark {
    position: absolute; left: 62px; top: 30px;
    font-family: "Montserrat", Arial, sans-serif;
    font-weight: 800; font-size: 26px; letter-spacing: .5px;
    color: var(--brand-blue); text-transform: uppercase; line-height: 1.1;
  }
  .phone-bar {
    position: absolute; left: 0; top: 116px;
    width: 250px; height: 48px;
    background: var(--ink);
    border-radius: 0 14px 14px 0;
    display: flex; align-items: center; gap: 10px; padding-left: 24px;
    color: #e9e9e9; font-size: 13px;
  }
  .name-band {
    position: absolute; right: 0; top: 110px;
    width: 255px; height: 60px;
    background: var(--brand-blue);
    border-radius: 14px 0 0 14px;
    color: var(--paper);
    padding: 10px 0 0 22px;
    font-family: "Montserrat", Arial, sans-serif;
  }
  .name-band__name { font-weight: 800; font-size: 21px; letter-spacing: .5px; }
  .name-band__company { font-weight: 500; font-size: 11.5px; letter-spacing: 1px; }
  .contact-list {
    position: absolute; left: 270px; top: 182px;
    list-style: none; font-size: 12px; color: var(--text);
  }
  .contact-list li { display: flex; align-items: flex-start; gap: 8px; margin-bottom: 4px; line-height: 1.2; }
  .icon-dot {
    flex: none; width: 18px; height: 18px; border-radius: 50%;
    background: var(--brand-blue); display: grid; place-items: center;
  }
  .icon-dot svg { width: 11px; height: 11px; }
  /* ---------- Back ---------- */
  .card--back {
    left: 635px; top: 300px;
    background: linear-gradient(135deg, var(--brand-blue) 0%, var(--brand-blue-dark) 100%);
  }
  .back__texture { position: absolute; inset: 0; background: linear-gradient(160deg, rgba(255,255,255,.05), rgba(0,0,0,.05)); }
  .back__tab-top {
    position: absolute; left: 0; top: 30px; width: 70px; height: 40px;
    background: var(--paper); border-radius: 0 12px 12px 0;
  }
  .back__wordmark {
    position: absolute; left: 90px; top: 62px;
    font-family: "Montserrat", Arial, sans-serif;
    font-weight: 800; font-size: 26px; letter-spacing: .5px;
    color: var(--paper); text-transform: uppercase; line-height: 1.1;
  }
  .back__web-tab {
    position: absolute; right: 0; top: 178px; width: 320px; height: 56px;
    background: var(--paper); border-radius: 14px 0 0 14px;
    display: flex; align-items: center; padding-left: 28px;
    font-family: "Montserrat", Arial, sans-serif; font-weight: 600;
    font-size: 11px; letter-spacing: 1.3px; color: var(--brand-blue);
    text-transform: uppercase; white-space: nowrap;
  }
</style>
</head>
<body>

<section class="card card--front">
  <div class="front__photo" role="img" aria-label="Faint photo of a bright modern kitchen with appliances"></div>
  <div class="front__corner front__corner--top"></div>
  <div class="front__corner front__corner--bottom"></div>

  <div class="wordmark">Brandon's<br>Appliances</div>

  <div class="phone-bar">
    <span class="icon-dot"><svg viewBox="0 0 24 24"><path fill="#fff" d="M6.6 10.8a15.1 15.1 0 0 0 6.6 6.6l2.2-2.2c.3-.3.7-.4 1-.2 1.1.4 2.3.6 3.6.6.6 0 1 .4 1 1V20c0 .6-.4 1-1 1A17 17 0 0 1 3 4c0-.6.4-1 1-1h3.5c.6 0 1 .4 1 1 0 1.3.2 2.5.6 3.6.1.3 0 .7-.2 1z"/></svg></span>
    <span>(555) 201-4837 - (555) 309-6152</span>
  </div>

  <div class="name-band">
    <div class="name-band__name">DANIEL MOORE</div>
    <div class="name-band__company">BRANDON'S APPLIANCES</div>
  </div>

  <ul class="contact-list">
    <li><span class="icon-dot"><svg viewBox="0 0 24 24"><path fill="none" stroke="#fff" stroke-width="2" d="M3 6h18v12H3zM3 6l9 7 9-7"/></svg></span>danielm@brandonsappliances.com</li>
    <li><span class="icon-dot"><svg viewBox="0 0 24 24"><g fill="none" stroke="#fff" stroke-width="2"><circle cx="12" cy="12" r="9"/><path d="M3 12h18M12 3c3 3 3 15 0 18M12 3c-3 3-3 15 0 18"/></g></svg></span>www.brandonsappliances.com</li>
    <li><span class="icon-dot"><svg viewBox="0 0 24 24"><path fill="#fff" d="M12 2a7 7 0 0 0-7 7c0 5 7 13 7 13s7-8 7-13a7 7 0 0 0-7-7zm0 9.5A2.5 2.5 0 1 1 12 6.5a2.5 2.5 0 0 1 0 5z"/></svg></span>148 Harbor View St. Lakeport,<br>CT 06010</li>
    <li><span class="icon-dot"><svg viewBox="0 0 24 24"><path fill="#fff" d="M12 2a7 7 0 0 0-7 7c0 5 7 13 7 13s7-8 7-13a7 7 0 0 0-7-7zm0 9.5A2.5 2.5 0 1 1 12 6.5a2.5 2.5 0 0 1 0 5z"/></svg></span>27 Millbrook Ave. Eastfield,<br>CT 06020</li>
  </ul>
</section>

<section class="card card--back">
  <div class="back__texture" role="img" aria-label="Subtle interlocking geometric pattern on blue"></div>
  <div class="back__tab-top"></div>
  <div class="back__wordmark">Brandon's<br>Appliances</div>
  <div class="back__web-tab">www.brandonsappliances.com</div>
</section>

</body>
</html>
```